B2B Energy Broker Website

Our current website looks amateur, we need something far more professional looking and advanced. Current website is www.kelmora-utilitylink.com

```html
<!DOCTYPE html>
<html lang="en">
<head>
<meta charset="utf-8">
<title>Kelmora Utilitylink — Transparent Energy Savings</title>
<link href="https://fonts.googleapis.com/css2?family=Lato:wght@300;400;700;900&family=Roboto:wght@400;500&display=swap" rel="stylesheet">
<style>
:root{
  --navy:#1d2354;
  --navy-deep:#1b2050;
  --heading:#1c2a5c;
  --blue:#2f70a9;
  --card-top:#2f82bf;
  --card-bottom:#1f65a1;
  --light:#f2f5f9;
  --grey-band:#e4e6ea;
  --text:#3b3f4a;
  --muted:#8a8f99;
  --white:#ffffff;
  --gold:#f3c21b;
}
*{box-sizing:border-box;margin:0;padding:0}
html,body{width:1200px;height:3058px;overflow:hidden;background:#fff}
body{font-family:"Lato",sans-serif;color:var(--text)}
.canvas{position:relative;width:1200px;height:3058px;overflow:hidden;background:#fff}
.abs{position:absolute}

/* top bar + nav */
.topbar{left:33px;top:4px;width:1135px;height:28px;background:var(--blue);color:#fff;font-size:11px;text-align:right;padding:8px 52px 0 0}
.brand{display:flex;align-items:center;gap:8px;font-size:17px;font-weight:700;color:#3a3f4a;letter-spacing:.5px}
.brand .dot{width:26px;height:26px;border-radius:50%;background:#3a3f4a}
.nav-brand{left:78px;top:44px}
.nav{top:50px;left:346px;display:flex;font-size:14px;color:#444}
.nav a{color:#444;text-decoration:none}
.nav .sep{color:#bbb}
.login{left:969px;top:48px;width:65px;height:19px;border-radius:10px;background:#4a4d55;color:#fff;font-size:10px;font-weight:700;text-align:center;line-height:19px;box-shadow:0 2px 3px rgba(0,0,0,.35)}

/* hero */
.hero{left:32px;top:100px;width:1136px;height:404px;background:linear-gradient(100deg,#4b8fb6 0%,#7fb7d4 35%,#3f7fa8 60%,#c07a3a 82%,#2a5f88 100%)}
.hero-title{left:32px;top:172px;width:1060px;text-align:center;font-family:"Roboto",sans-serif;font-size:38px;font-weight:500;letter-spacing:2px;color:#4a4f57}
.hero-sub{left:32px;top:238px;width:1040px;text-align:center;font-family:"Roboto",sans-serif;font-size:18px;letter-spacing:1.5px;color:#3f4550}

/* welcome */
.welcome{left:26px;top:504px;width:1135px;height:536px;background:var(--light)}
.welcome-kicker{left:0;top:520px;width:1230px;text-align:center;font-size:21px;color:#333}
.welcome-name{left:0;top:560px;width:1230px;text-align:center;font-size:31px;font-weight:700;color:var(--heading)}
.why-title{left:51px;top:652px;width:420px;font-size:25px;font-weight:700;color:var(--heading);line-height:35px}
.why-text{left:51px;top:748px;width:455px;font-size:13.5px;font-weight:300;line-height:21.5px;color:#2d3038}
.btn{background:var(--navy);color:#fff;font-size:12.5px;font-weight:700;text-align:center;border-radius:5px;box-shadow:0 2px 4px rgba(0,0,0,.3)}
.read-more{left:51px;top:917px;width:102px;height:32px;line-height:32px}
.photo{border:3px solid #fff;box-shadow:0 2px 8px rgba(0,0,0,.25)}
.photo-wind{left:636px;top:651px;width:303px;height:302px;background:linear-gradient(160deg,#b8b8b2 0%,#d9a35c 55%,#6b7a4a 100%)}
.photo-bulb{left:828px;top:840px;width:296px;height:183px;background:radial-gradient(circle at 50% 45%,#f5e68a 0%,#a9c23a 40%,#3f6e1f 100%)}

/* services */
.band{left:24px;top:1046px;width:1137px;height:330px;background:linear-gradient(180deg,var(--grey-band) 0%,#fff 45%)}
.card{top:1091px;height:263px;border-radius:10px;background:linear-gradient(180deg,var(--card-top),var(--card-bottom));color:#fff;padding:28px 26px 0;box-shadow:0 3px 6px rgba(0,0,0,.2)}
.card svg{display:block;height:70px}
.card h3{font-size:13px;font-weight:700;letter-spacing:2px;margin-top:22px}
.card p{font-size:12.5px;font-weight:300;line-height:17.5px;margin-top:18px;width:200px}
.c1{left:51px;width:260px}.c2{left:331px;width:257px}.c3{left:607px;width:258px}.c4{left:885px;width:257px}

.cta{left:51px;top:1379px;width:1091px;height:62px;background:linear-gradient(90deg,#2f78b4,#1f3f7c 80%,var(--navy));color:#fff;font-size:23px;font-weight:700;text-align:center;line-height:62px;box-shadow:0 3px 5px rgba(0,0,0,.25)}

/* features */
.feat-frame{left:51px;top:1465px;width:532px;height:410px;background:#f1f1f1;padding:11px;box-shadow:0 2px 5px rgba(0,0,0,.2)}
.feat-photo{width:100%;height:100%;background:radial-gradient(circle at 82% 45%,#f7c14a 0%,#b06a1e 20%,#3c4a18 50%,#1b220e 100%)}
.panel{left:601px;top:1465px;width:541px;height:410px;background:var(--navy-deep);color:#fff}
.feat{position:absolute;left:33px;width:480px}
.feat svg{position:absolute;left:0;top:0}
.feat h4{position:absolute;left:76px;top:0;font-size:16.5px;font-weight:700}
.feat p{position:absolute;left:76px;top:28px;width:400px;font-size:13px;font-weight:300;line-height:18px;color:#dfe2ee}
.rule{position:absolute;left:33px;width:483px;height:1px;background:#7a80a8}

/* suppliers */
.suppliers{left:48px;top:1909px;width:1090px;height:90px;background:#fff;box-shadow:0 2px 6px rgba(0,0,0,.18);display:flex;align-items:center;justify-content:space-around;padding:0 20px}
.suppliers span{display:flex;align-items:center;gap:7px;font-size:19px;font-weight:700;color:#2a3a78}
.suppliers i{width:18px;height:18px;border-radius:50%;background:#2a3a78;display:block}

/* testimonials */
.tcard{top:2037px;height:280px;background:#fff;box-shadow:0 1px 4px rgba(0,0,0,.1)}
.t1{left:50px;width:550px}.t2{left:606px;width:532px}
.tphoto{position:absolute;left:0;top:0;height:280px;border-radius:16px 0 0 0;background:linear-gradient(180deg,#2d78b8 0%,#2666a8 58%,#232a72 58%,#232a72 100%)}
.t1 .tphoto{width:245px}.t2 .tphoto{width:237px}
.portrait{position:absolute;top:33px;width:160px;height:160px;border-radius:50%;border:4px solid #fff}
.t1 .portrait{left:42px;background:linear-gradient(180deg,#dfe4ea,#3d6f9c)}
.t2 .portrait{left:38px;background:linear-gradient(180deg,#e4dad2,#d2662f)}
.stars{position:absolute;top:228px;width:100%;text-align:center;color:var(--gold);font-size:19px;letter-spacing:2px}
.quote{position:absolute;top:26px;font-family:Georgia,serif;font-size:90px;line-height:90px;color:#c9c9c9;font-weight:700}
.tname{position:absolute;top:82px;font-size:14px;font-weight:700;color:#1d1d1d}
.trole{position:absolute;top:100px;font-size:7.5px;color:#999;letter-spacing:.3px}
.tbody{position:absolute;top:126px;width:280px;font-size:8.6px;font-weight:700;line-height:21.5px;color:#8d8d8d;letter-spacing:.2px}
.t1 .quote,.t1 .tname,.t1 .trole,.t1 .tbody{left:259px}
.t2 .quote,.t2 .tname,.t2 .trole,.t2 .tbody{left:252px}

/* faq + footer */
.faq{left:51px;top:2367px;width:1087px;height:668px;background:#e9ebee;overflow:hidden}
.faq-h{left:216px;top:2410px;font-size:20px;font-weight:900;color:#111}
.faq-q{left:216px;top:2460px;width:420px;font-size:18.5px;font-weight:700;color:#111;line-height:23px}
.faq-a{left:216px;top:2521px;width:770px;font-size:14px;color:#333;line-height:21.5px}
.view-more{left:546px;top:2643px;width:103px;height:32px;line-height:32px}
.wave{left:51px;top:2700px}
.fbrand{left:78px;top:2833px;color:#fff}
.fbrand .dot{background:#fff}
.f-name{left:76px;top:2896px;font-size:13.5px;color:#fff}
.f-copy{left:74px;top:2925px;font-size:11px;color:#fff}
.fcol{top:2838px;color:#fff}
.fcol h5{font-size:15.5px;font-weight:700;margin-bottom:21px}
.fcol li{list-style:none;font-size:11px;line-height:28.3px}
.col-home{left:362px}.col-about{left:557px}.col-serv{left:734px}
.follow{left:936px;top:2838px;color:#fff;font-size:15.5px;font-weight:700}
.social{left:928px;top:2920px;display:flex;gap:12px}
.social span{width:40px;height:24px;border-radius:4px;font-size:9.5px;font-weight:700;color:#fff;text-align:center;line-height:24px}
</style>
</head>
<body>
<div class="canvas">

  <div class="abs topbar">Tel: 0333 555 0147 | info@kelmora-utilitylink.com</div>
  <div class="abs brand nav-brand"><span class="dot"></span>Kelmora Utilitylink</div>
  <nav class="abs nav">
    <a href="#" style="width:70px">Home</a><span class="sep" style="width:35px">|</span>
    <a href="#" style="width:77px">About</a><span class="sep" style="width:30px">|</span>
    <a href="#" style="width:125px">Contact Us</a><span class="sep" style="width:38px">|</span>
    <a href="#" style="width:90px">Service</a><span class="sep">|</span>
  </nav>
  <div class="abs login">Log in</div>

  <div class="abs hero" role="img" aria-label="Two engineers in hard hats and safety vests pointing across power infrastructure, overlaid with glowing energy icons"></div>
  <div class="abs hero-title">TRANSPARENT ENERGY SAVINGS</div>
  <div class="abs hero-sub">UNBIASED FOR YOUR BUSINESS</div>

  <div class="abs welcome"></div>
  <div class="abs welcome-kicker">WELCOME TO</div>
  <div class="abs welcome-name">KELMORA UTILITYLINK</div>
  <h2 class="abs why-title">WHY CHOOSE OUR ENERGY SOLUTIONS SERVICE</h2>
  <p class="abs why-text">Along with providing competitive business energy procurement, we run a complete service solution for your ongoing energy requirements. We can take total management of your bills, supplier relationship, renewals and more. If you are concerned about a more complex arrangement for your energy supply then we will endeavour to take over the time spent on it and allow you as much or as little involvement as you desire.</p>
  <div class="abs btn read-more">Read More</div>
  <div class="abs photo photo-wind" role="img" aria-label="Engineers in hard hats beside wind turbines at sunset"></div>
  <div class="abs photo photo-bulb" role="img" aria-label="Hand holding a light bulb surrounded by green energy icons"></div>

  <div class="abs band"></div>
  <div class="abs card c1">
    <svg viewBox="0 0 50 70" width="50" fill="none" stroke="#fff" stroke-width="2.5"><rect x="14" y="2" width="22" height="12" rx="2"/><rect x="4" y="14" width="42" height="52" rx="8"/><path d="M25 54c-7 0-10-6-7-12 2-4 5-6 5-10 5 4 10 9 8 16-1 4-3 6-6 6z"/></svg>
    <h3>COMMERCIAL GAS</h3>
    <p>We offer an impartial review of your business gas  requirements to ensure you are getting the best price s, service and management as a total package.</p>
  </div>
  <div class="abs card c2">
    <svg viewBox="0 0 80 70" width="80" fill="none" stroke="#fff" stroke-width="2.5"><path d="M10 6l-6 16h10l-6 16"/><path d="M38 12c-6 6-10 10-6 18 3 4 9 4 12 0 4-6-2-12-6-18z"/><path d="M64 8c-6 8-8 12-6 18 2 5 10 5 12 0 2-6 0-10-6-18z"/><rect x="4" y="48" width="14" height="14"/><rect x="32" y="48" width="14" height="14"/><rect x="60" y="48" width="14" height="14"/><path d="M7 51l8 8M15 51l-8 8M35 51l8 8M43 51l-8 8M63 51l8 8M71 51l-8 8"/></svg>
    <h3>COMMERCIAL ELECTRICITY</h3>
    <p>We offer an impartial review of your business gas  requirements to ensure you are getting the best price s, service and management as a total package.</p>
  </div>
  <div class="abs card c3">
    <svg viewBox="0 0 76 70" width="76" fill="none" stroke="#fff" stroke-width="2.5"><path d="M20 26c-8 10-16 18-16 28a16 16 0 0032 0c0-10-8-18-16-28z"/><path d="M40 2c-4 6-8 10-8 15a8 8 0 0016 0c0-5-4-9-8-15z"/><path d="M62 20c-5 7-10 12-10 18a10 10 0 0020 0c0-6-5-11-10-18z"/></svg>
    <h3>COMMERCIAL WATER</h3>
    <p>We offer an impartial review of your business gas  requirements to ensure you are getting the best price s, service and management as a total package.</p>
  </div>
  <div class="abs card c4">
    <svg viewBox="0 0 70 70" width="70" fill="none" stroke="#fff" stroke-width="2.5"><path d="M22 60A30 30 0 1150 62"/><path d="M28 12v12M42 12v12"/><path d="M22 24h26v8a13 13 0 01-26 0z"/><path d="M35 45v18"/></svg>
    <h3>UTILITY SERVICES</h3>
    <p>We offer an impartial review of your business gas  requirements to ensure you are getting the best price s, service and management as a total package.</p>
  </div>

  <div class="abs cta">Contact Kelmora Now On 0333 555 0147 To Start Saving</div>

  <div class="abs feat-frame"><div class="feat-photo" role="img" aria-label="Seedlings growing in soil along a rising line chart ending in a glowing light bulb"></div></div>
  <div class="abs panel">
    <div class="feat" style="top:52px">
      <svg width="50" height="40" viewBox="0 0 50 40" fill="none" stroke="#fff" stroke-width="3"><path d="M3 2v35h45"/><path d="M8 30l12-14 8 8 16-16"/><path d="M36 8h8v8"/></svg>
      <h4>Market Trend Analysis</h4>
      <p>Our energy analysts monitor a live energy market curve to ensure you buy at the right time and save as much as possible.</p>
    </div>
    <div class="rule" style="top:145px"></div>
    <div class="feat" style="top:171px">
      <svg width="44" height="44" viewBox="0 0 44 44" fill="none" stroke="#fff" stroke-width="4"><rect x="3" y="3" width="18" height="12" rx="6" transform="rotate(45 12 9)"/><rect x="22" y="25" width="18" height="12" rx="6" transform="rotate(45 31 31)"/><path d="M16 16l12 12"/></svg>
      <h4>Direct Relationships</h4>
      <p>We hold direct relationships with over 18 major suppliers, we use these relationships to ensure you get the most from your supplier.</p>
    </div>
    <div class="rule" style="top:265px"></div>
    <div class="feat" style="top:285px">
      <svg width="42" height="42" viewBox="0 0 42 42"><circle cx="21" cy="21" r="19" fill="#fff"/><path d="M10 12c5 0 7 4 6 8s-6 3-6 8c-3-3-5-10 0-16zM26 6c4 4 2 8 5 10s5 6 2 12c-3 4-8 2-8-3s-4-8 1-19z" fill="var(--navy-deep)"/></svg>
      <h4>Industry Experience</h4>
      <p>Our two founders hold over 30 years industry experience between them and our staff are what we believe to be the best in the industry.</p>
    </div>
  </div>

  <div class="abs suppliers">
    <span><i></i>Northgate Gas</span>
    <span><i></i>Ivel Energy</span>
    <span><i></i>Twinline Power</span>
    <span><i></i>Sarn Electric</span>
    <span><i></i>Halo Fuel</span>
    <span><i></i>Verra Energies</span>
    <span><i></i>Ostra Power</span>
  </div>

  <div class="abs tcard t1">
    <div class="tphoto"><div class="portrait" role="img" aria-label="Portrait of a smiling man in a blue suit"></div><div class="stars">★★★★★</div></div>
    <div class="quote">&ldquo;</div>
    <div class="tname">AREN VOSS</div>
    <div class="trole">CHIEF ENGINEER</div>
    <div class="tbody">LOREM IPSUM DOLOR SIT AMET, CONSECTETUR ADIPISCING ELIT. LOBORTIS LOREM FAUCIBUS MAECENAS SAPIEN. AMET VARIUS RHONCUS SIT AT AUGUE SIT SODALES POSUERE. SED NULLA DICTUM ID SCELERISQUE MAECENAS NISI QUIS VESTIBULUM. ALIQUET FACILISIS DUIS AC UT EU.</div>
  </div>
  <div class="abs tcard t2">
    <div class="tphoto"><div class="portrait" role="img" aria-label="Portrait of a smiling woman in an orange jacket"></div><div class="stars">★★★★★</div></div>
    <div class="quote">&ldquo;</div>
    <div class="tname">MIRA TALLIS</div>
    <div class="trole">MANAGING DIRECTOR</div>
    <div class="tbody">LOREM IPSUM DOLOR SIT AMET, CONSECTETUR ADIPISCING ELIT. LOBORTIS LOREM FAUCIBUS MAECENAS SAPIEN. AMET VARIUS RHONCUS SIT AT AUGUE SIT SODALES POSUERE. SED NULLA DICTUM ID SCELERISQUE MAECENAS NISI QUIS VESTIBULUM. ALIQUET FACILISIS DUIS AC UT EU.</div>
  </div>

  <div class="abs faq"></div>
  <h3 class="abs faq-h">FAQs</h3>
  <h4 class="abs faq-q">WHY SHOULD MY BUSINESS USE KELMORA UTILITYLINK?</h4>
  <p class="abs faq-a">We provide an unbiased &amp; transparent cost effective solution to all your business energy needs. In essence, with over 3 decades experience in the UK energy Industry. We have both the expertise &amp; know how to manage your business energy requirements.  Our philosophy is simple solutions with transparency.</p>
  <div class="abs btn view-more">View More</div>

  <svg class="abs wave" width="1087" height="335" viewBox="0 0 1087 335"><path d="M0 120C180 50 360 26 543 26S900 50 1087 120V335H0Z" fill="var(--navy-deep)"/></svg>

  <div class="abs brand fbrand"><span class="dot"></span>Kelmora Utilitylink</div>
  <div class="abs f-name">KELMORA-UTILITYLINK</div>
  <div class="abs f-copy">© 2022 It kelmora-utilitylink. All rights reserved.</div>
  <div class="abs fcol col-home"><h5>HOME</h5><ul><li>About Us</li><li>Gallery</li><li>Service</li><li>Prices</li><li>Contacts</li></ul></div>
  <div class="abs fcol col-about"><h5>About us</h5><ul><li>Basic Plan</li><li>Business Plan</li><li>Exclusive Plan</li><li>Free Plan</li><li>Standard Plan</li></ul></div>
  <div class="abs fcol col-serv"><h5>Services</h5><ul><li>Sell on Eco</li><li>Advertises on Eco</li><li>Affiliate Program</li><li>Privacy &amp; Policy</li><li>Partnership</li></ul></div>
  <div class="abs follow">Follow</div>
  <div class="abs social"><span>Fenlo</span><span>Chirra</span><span>Plexa</span><span>Workly</span></div>

</div>
</body>
</html>
```